Flier redesign

Sample fliers are attached from previous 2 years "Seasonal care 2018" and "2019 Seasonal Care" . Need an updated design for this year.

Possible images are attached to this brief. If you use the before/after pictures - you should use both of them. Use images attached to this brief or any from our website that you may prefer.

Colors

Designer to choose colors to be used in the design.

Requirements
Must have
• Colors should match our website theme. www.oakmerefieldgrounds.org
• Should be a "new" design, not just copying one of the prior year designs with a different image.
• Must be created in photoshop and file must be provided at the end.
• Text should be the same as 2019 version.

```html
<!DOCTYPE html>
<html lang="en">
<head>
<meta charset="utf-8">
<title>Oakmere Cemetery – 2020 Gravesite Landscaping Packages</title>
<link href="https://fonts.googleapis.com/css2?family=Cormorant+SC:wght@700&family=Open+Sans:wght@400;600&display=swap" rel="stylesheet">
<style>
  :root{
    --maroon:#7b1a2d;
    --gold:#c4b57c;
    --gold-text:#9a8a4c;
    --gold-light:#d8cc9b;
    --grey-bg:#e7e8ea;
    --body:#555459;
    --white:#ffffff;
  }
  *{margin:0;padding:0;box-sizing:border-box}
  html,body{width:996px;height:1200px;overflow:hidden;background:#fff}
  .flier{position:relative;width:996px;height:1200px;overflow:hidden;font-family:"Open Sans",sans-serif;background:var(--white)}
  .backdrop{position:absolute;inset:0}
  .masthead{position:absolute;top:58px;left:0;width:100%;display:flex;justify-content:center;align-items:center;gap:16px}
  .masthead .dot{width:34px;height:34px;border-radius:50%;background:var(--maroon)}
  .masthead .name{font-family:"Open Sans",sans-serif;font-weight:600;font-size:44px;color:var(--maroon);line-height:1}
  .badge{position:absolute;left:602px;top:463px;width:104px;height:104px}
  .badge span{position:absolute;inset:0;display:flex;flex-direction:column;justify-content:center;align-items:center;color:#fff;font-size:15px;line-height:1.25}
  .card{position:absolute;background:var(--white);border-radius:22px;overflow:hidden;box-shadow:0 2px 6px rgba(0,0,0,.12);text-align:center}
  .card.seasonal{left:42px;top:568px;width:298px;height:470px}
  .card.perpetual{left:357px;top:525px;width:298px;height:513px}
  .card.basic{left:667px;top:568px;width:298px;height:470px}
  .cap{background:var(--maroon);height:98px;clip-path:polygon(0 0,100% 0,100% 78%,50% 100%,0 78%);display:flex;align-items:center;justify-content:center;padding-bottom:14px}
  .cap h2{color:var(--gold-light);font-weight:600;font-size:20px;letter-spacing:1.4px;line-height:1.35}
  .tagline{color:var(--maroon);font-size:15.5px;line-height:1.3;margin:12px 20px 0}
  .features{list-style:none;text-align:left;margin:20px 44px 0 28px}
  .features li{position:relative;padding-left:26px;color:var(--body);font-size:14.8px;line-height:1.12;margin-bottom:6px}
  .features li::before{content:"";position:absolute;left:0;top:1px;width:14px;height:14px;border:1.3px solid var(--gold-text);border-radius:50%}
  .features li::after{content:"";position:absolute;left:4px;top:5.5px;width:4px;height:4px;border-top:1.3px solid var(--gold-text);border-right:1.3px solid var(--gold-text);transform:rotate(45deg)}
  .features.tight{margin-top:14px;margin-right:38px}
  .features.tight li{margin-bottom:4px}
  .terms{position:absolute;left:0;right:0;display:flex;justify-content:center}
  .terms div{padding:0 8px;border-left:1px solid #bbb}
  .terms div:first-child{border-left:none}
  .terms small{display:block;color:var(--gold-text);font-size:14.5px}
  .terms strong,.price{color:var(--maroon);font-weight:600;font-size:27px;line-height:1.2}
  .monthly{position:absolute;left:0;right:0;color:var(--gold-text);font-size:15px;letter-spacing:.4px}
  .price{position:absolute;left:0;right:0}
  .note{position:absolute;left:0;right:0;bottom:22px;color:var(--gold-text);font-size:11.5px;line-height:1.35}
  .footer-title{position:absolute;left:36px;top:1117px;display:flex;align-items:center;gap:14px;color:#fff}
  .footer-title .year{font-family:"Cormorant SC",serif;font-weight:700;font-size:68px;line-height:1}
  .footer-title .label{font-size:16.5px;letter-spacing:.8px;line-height:1.1}
  .contact{position:absolute;right:16px;top:1112px;list-style:none;color:#fff;font-size:15.5px;text-align:right}
  .contact li{display:flex;justify-content:flex-end;align-items:center;gap:10px;height:27px}
  .contact svg{width:20px;height:20px}
</style>
</head>
<body>
<div class="flier">
  <svg class="backdrop" width="996" height="1200" viewBox="0 0 996 1200">
    <defs>
      <linearGradient id="grounds" x1="0" y1="0" x2="0" y2="1">
        <stop offset="0" stop-color="#c9a86a"/>
        <stop offset=".45" stop-color="#9a8a52"/>
        <stop offset=".7" stop-color="#7f9a4a"/>
        <stop offset="1" stop-color="#6e8e3c"/>
      </linearGradient>
    </defs>
    <rect x="0" y="600" width="996" height="520" fill="var(--grey-bg)"/>
    <path d="M0,100 Q498,240 996,100 L996,132 Q498,262 0,132 Z" fill="var(--gold)"/>
    <path d="M0,120 Q498,262 996,120 L996,690 Q498,560 0,690 Z" fill="url(#grounds)" role="img" aria-label="Photograph of cemetery grounds in autumn with a red maple tree, winding road and rows of headstones"/>
    <path d="M0,690 Q498,560 996,690" fill="none" stroke="var(--gold)" stroke-width="8"/>
    <rect x="0" y="1102" width="996" height="98" fill="var(--maroon)"/>
    <path d="M0,1050 Q260,1040 446,1200 L0,1200 Z" fill="var(--gold)" stroke="#fff" stroke-width="5"/>
  </svg>

  <header class="masthead">
    <span class="dot"></span>
    <span class="name">Oakmere Cemetery</span>
  </header>

  <div class="card seasonal">
    <div class="cap"><h2>SEASONAL<br>CARE</h2></div>
    <p class="tagline">Seasonal landscaping<br>grave care</p>
    <ul class="features" style="margin-top:26px">
      <li>Weeding and trimming services on your gravesite approximately every 7 weeks during the growing season: mid-April through mid-October</li>
    </ul>
    <div class="terms" style="top:322px">
      <div><small>3 YEARS</small><strong>$345</strong></div>
      <div><small>2 YEARS</small><strong>$230</strong></div>
      <div><small>1 YEARS</small><strong>$115</strong></div>
    </div>
    <p class="note">Multi-year payment locks in current rates.<br>Valid trough 10/31/20.</p>
  </div>

  <div class="card perpetual">
    <div class="cap"><h2>PERPETUAL CARE<br>ENDOWMENT</h2></div>
    <p class="tagline">Landscaping care forever for<br>graves with plantings</p>
    <ul class="features tight">
      <li>Weeding and trimming services on your gravesite approximately every 7 weeks during the growing season: mid-April through mid-October</li>
      <li>Monument leveling</li>
      <li>Payment ensures grave care forever</li>
      <li>Full bed of boxwood shrubs</li>
      <li>Replacement of shrubs</li>
      <li>Trust certificate</li>
    </ul>
    <p class="monthly" style="top:408px">12 MONTHLY PAYMENTS OF</p>
    <p class="price" style="top:428px">$297</p>
    <p class="note">Call for single payment discount.<br>Valid trough 10/31/20.</p>
  </div>

  <div class="card basic">
    <div class="cap"><h2>BASIC CARE<br>ENDOWMENT</h2></div>
    <p class="tagline">Landscaping forever for<br>graves with no plantings</p>
    <ul class="features" style="margin-top:26px">
      <li>Weeding and trimming services on your gravesite 2 times per year: mid-May and mid-September</li>
      <li style="margin-top:14px">Monument leveling</li>
      <li style="margin-top:10px">Payment ensures grave care forever</li>
    </ul>
    <p class="monthly" style="top:365px">12 MONTHLY PAYMENTS OF</p>
    <p class="price" style="top:385px">$239</p>
    <p class="note">Call for single payment discount.<br>Valid trough 10/31/20.</p>
  </div>

  <div class="badge">
    <svg width="104" height="104" viewBox="0 0 104 104">
      <polygon fill="var(--gold)" points="52,2 58,12 68,5 71,17 82,13 82,25 94,24 90,36 101,40 94,50 102,58 92,64 97,75 85,78 87,90 75,89 72,101 61,95 52,103 43,95 32,101 29,89 17,90 19,78 7,75 12,64 2,58 10,50 3,40 14,36 10,24 22,25 22,13 33,17 36,5 46,12"/>
    </svg>
    <span>MOST<br>POPULAR</span>
  </div>

  <div class="footer-title">
    <span class="year">2020</span>
    <span class="label">GRAVESITE<br>LANDSCAPING<br>PACKAGES</span>
  </div>

  <ul class="contact">
    <li>(201) 555-0148
      <svg viewBox="0 0 20 20"><circle cx="10" cy="10" r="8.5" fill="none" stroke="var(--gold-light)" stroke-width="1.5"/><path d="M7 5.5l1.6 2.4-1 1.1c.7 1.4 1.6 2.3 3 3l1.1-1 2.4 1.6-1 1.6c-3.4-.2-6.5-3.3-6.7-6.7z" fill="var(--gold-light)"/></svg>
    </li>
    <li>www.oakmerefieldgrounds.org | info@oakmerefieldgrounds.org
      <svg viewBox="0 0 20 20"><circle cx="10" cy="10" r="8.5" fill="none" stroke="var(--gold-light)" stroke-width="1.5"/><circle cx="10" cy="10" r="2.2" fill="none" stroke="var(--gold-light)" stroke-width="1.3"/><path d="M12.2 8v3c0 1.4 2 1.4 2 0V10a4.2 4.2 0 1 0-1.6 3.3" fill="none" stroke="var(--gold-light)" stroke-width="1.3"/></svg>
    </li>
    <li>48 Alder Ln., Fairbrook, NJ 07099
      <svg viewBox="0 0 20 20"><circle cx="10" cy="10" r="8.5" fill="none" stroke="var(--gold-light)" stroke-width="1.5"/><path d="M10 15s-3.5-3.6-3.5-6a3.5 3.5 0 0 1 7 0c0 2.4-3.5 6-3.5 6z" fill="none" stroke="var(--gold-light)" stroke-width="1.3"/><circle cx="10" cy="9" r="1.2" fill="var(--gold-light)"/></svg>
    </li>
  </ul>
</div>
</body>
</html>
```